Lumora aesthetics offers a range of facial aesthetics treatments by a fully qualified dentist, to a high end crowd. Treatments include antiwrinkle treatment, the use of dermal fillers to provide facial volumisation and rejuvenation and also lip volumisation.
I want a luxurious and bold look. Black background with a bold striking gold logo in the centre possibly incorporating the outline of a face in a subtle yet effective way. I want it to include the work I offer so people will be aware of what they are looking into but not look like there's too much on the card, So it's a clean look.
At the bottom I would like it to say by Dr. Meera Sandhu. Alongside my email address and mobile number.

```html
<!DOCTYPE html>
<html lang="en">
<head>
<meta charset="utf-8">
<title>Lumora aesthetics business cards</title>
<link href="https://fonts.googleapis.com/css2?family=PT+Sans:wght@400;700&family=Open+Sans:wght@400;600;700&display=swap" rel="stylesheet">
<style>
  :root {
    --backdrop: #ecebea;
    --card-white: #ffffff;
    --card-black: #1c1b1c;
    --card-back: #1f1d1e;
    --pattern-tone: #2a2829;
    --gold: #d9a718;
    --gold-bright: #f0c419;
    --gold-line: #e3b511;
    --text-light: #f2f2f2;
  }
  html, body {
    margin: 0;
    padding: 0;
    width: 1200px;
    height: 900px;
    overflow: hidden;
    background: var(--backdrop);
  }
  .canvas {
    position: relative;
    width: 1200px;
    height: 900px;
  }
  .card {
    position: absolute;
    box-shadow: 0 6px 18px rgba(0,0,0,0.18);
    overflow: hidden;
  }
  /* Front card */
  .card-front {
    left: 78px;
    top: 35px;
    width: 587px;
    height: 363px;
    background: var(--card-black);
  }
  .front-header {
    position: absolute;
    left: 0; top: 0;
    width: 100%;
    height: 197px;
    background: var(--card-white);
    display: flex;
    align-items: center;
    justify-content: center;
  }
  .front-divider {
    position: absolute;
    left: 0; top: 197px;
    width: 100%;
    height: 6px;
    background: var(--gold-line);
  }
  .brand-title {
    margin: 0;
    font-family: "PT Sans", sans-serif;
    font-weight: 400;
    font-size: 54px;
    letter-spacing: 0.5px;
    color: var(--gold);
    transform: translateY(-2px);
  }
  .practitioner {
    position: absolute;
    left: 0; top: 250px;
    width: 100%;
    text-align: center;
    font-family: "Open Sans", sans-serif;
    font-weight: 600;
    font-size: 19px;
    color: var(--gold-bright);
    letter-spacing: 0.3px;
    margin: 0;
  }
  .contact {
    position: absolute;
    left: 0; top: 297px;
    width: 100%;
    display: flex;
    justify-content: center;
    gap: 28px;
    font-family: "Open Sans", sans-serif;
    font-size: 17px;
    color: var(--text-light);
    margin: 0;
  }
  .contact-label {
    color: var(--gold-bright);
    font-weight: 700;
  }
  /* Back card */
  .card-back {
    left: 388px;
    top: 505px;
    width: 567px;
    height: 350px;
    background: var(--card-back);
  }
  .back-pattern {
    position: absolute;
    inset: 0;
    background: linear-gradient(135deg, var(--pattern-tone), var(--card-back));
  }
  .back-mark {
    position: absolute;
    left: 50%;
    top: 100px;
    transform: translateX(-50%);
    width: 84px;
    height: 84px;
    border-radius: 50%;
    background: var(--gold);
  }
  .back-name {
    position: absolute;
    left: 0; top: 208px;
    width: 100%;
    text-align: center;
    margin: 0;
    font-family: "PT Sans", sans-serif;
    font-weight: 400;
    font-size: 45px;
    color: var(--gold);
  }
</style>
</head>
<body>
<main class="canvas">
  <section class="card card-front">
    <header class="front-header">
      <h1 class="brand-title">Lumora aesthetics</h1>
    </header>
    <div class="front-divider"></div>
    <p class="practitioner">DR. MEERA SANDHU</p>
    <p class="contact">
      <span><span class="contact-label">P:</span> (044)987650321</span>
      <span><span class="contact-label">E:</span> hello@lumoraclinic.com</span>
    </p>
  </section>

  <section class="card card-back">
    <div class="back-pattern" role="img" aria-label="Subtle repeating monogram pattern in dark grey across the card background"></div>
    <div class="back-mark"></div>
    <p class="back-name">Lumora aesthetics</p>
  </section>
</main>
</body>
</html>
```